Announcement for a New Trauma Therapy Group - Rack Card

I need a two-sided "rack" card that is 4x9 announcing a Women's Trauma and Loss Group. I am a licensed therapist and will be starting this support group for women who have experienced trauma of all kinds. In addition to groups, I offer individual, couples, and family counseling sessions.

I would like to see designs that are soft tones and use colors like muted blues, greens, and sand tones. The final design should communicate hope and healing as well as have a peaceful feel to it.

I would like a picture of a woman's profile from either the side or from behind her. (possibly a contemplative picture on a beach)

I am attaching a picture of myself to go alongside the bio information as well.

On One Side, I need the description of the group and contact info:

Mending the Weary Spirit
Women's Trauma & Loss Group
Led by Licensed Professional Counselor, Jen Dalby Rusk

10 Week Group
Cost - $35 session
Group size limited to 10 participants

Topics Include:
What is Trauma?
How Trauma Affects Us
Creating a Feeling of Safety
Managing Trauma Triggers
Importance of Self Care
Healthy vs. Unhealthy Coping
Guilt, Shame, and Blame
Victim vs. Victimized
Grieving through Loss
Anger and Forgiveness
Imagining a Better Future

For More Information, Contact:
Jen Dalby Rusk, LPC, LMFT
(555) 614-3920
jen@brightmeadowcare.example

On Side Two:

Life hurts and does not seem fair. So what do you do when you are faced with an event in your life that knocks you off your feet? It seems no one understands what you are feeling and no one knows just what to say. It is tempting to pull away and isolate or put up a mask and pretend everything is OK.

It is my desire you know that you are not alone! There are others who understand the feelings you are going through and offer a safe place for encouraging support. I want to invite you to embark on a courageous journey of healing where you will not only learn how to "survive" after trauma and loss, but instead, learn that you can once again "thrive"!
- Jen Dalby Rusk, LPC, LMFT

Jen Dalby Rusk is a Licensed Professional Counselor and Licensed Marriage and Family Therapist. She is the owner of Quiet Harbor Counseling Services located in Tulsa, OK.

Jen is a trauma survivor herself and understands firsthand the unique challenges that can arise on the journey to healing.

(Include Jen's picture next to bio)

(Attach logo and business information to this side as well.)

Target Market(s)

Women who have gone through a traumatic experience or loss and are hurting emotionally

Industry/Entity Type

Counsellor

Font styles to use
Serif
Script

Colors
fbe7d2
86cfc6
cfeae6
85abd2
cfdeed

Requirements
Must have
• Jen's picture as well as her logo and contact information must be on the card.
• One side of the card should describe the group with the following description:
• "Mending the Weary Spirit"
• Women's Trauma & Loss Group
• Led by Licensed Professional Counselor, Jen Dalby Rusk
• 10 Week Group
• Cost - $35 session
• Group size limited to 10 participants
• Topics Include:
• What is Trauma?
• How Trauma Affects Us
• Creating a Feeling of Safety
• Managing Trauma Triggers
• Importance of Self Care
• Healthy vs. Unhealthy Coping
• Guilt, Shame, and Blame
• Victim vs. Victimized
• Grieving through Loss
• Anger and Forgiveness
• Imagining a Better Future
• For More Information, Contact:
• Jen Dalby Rusk, LPC, LMFT
• (555) 614-3920
• jen@brightmeadowcare.example
• On the second side, it must have this note from Jen:
• Life hurts and does not seem fair. So what do you do when you are faced with an event in your life that knocks you off your feet? It seems no one understands what you are feeling and no one knows just what to say. It is tempting to pull away and isolate or put up a mask and pretend everything is OK.
• It is my desire you know that you are not alone! There are others who understand the feelings you are going through and offer a safe place for encouraging support. I want to invite you to embark on a courageous journey of healing where you will not only learn how to "survive" after trauma and loss, but instead, learn that you can once again "thrive"!
• - Jen Dalby Rusk, LPC, LMFT
• Jen Dalby Rusk is a Licensed Professional Counselor and Licensed Marriage and Family Therapist. She is the owner of Quiet Harbor Counseling Services located in Tulsa, OK.
• Jen is a trauma survivor herself and understands firsthand the unique challenges that can arise on the journey to healing. In addition to facilitating groups, Jen also offers individual, marriage, and family counseling.
Nice to have
• soft muted colors that are peaceful. Light blues, greens, sand colors would work well. A picture at the top of the card of either a woman or a woman's profile that is hopeful such as a woman sitting at a beach overlooking the ocean.
Should not have
• No harsh or bright bold colors. This card needs to have a peaceful feeling to it.

```html
<!DOCTYPE html>
<html lang="en">
<head>
<meta charset="utf-8">
<title>Mending the Weary Spirit – Rack Card</title>
<link rel="stylesheet" href="https://fonts.googleapis.com/css2?family=Yellowtail&family=Marcellus&family=Roboto+Condensed:ital,wght@0,400;0,700;1,700&display=swap">
<style>
  :root{
    --green:#6aa843;
    --green-deep:#5a9a35;
    --lime:#b2f07f;
    --ink:#161616;
    --paper:#ffffff;
    --backdrop:#e9ebe9;
    --teal-line:#8fd3cb;
  }
  *{box-sizing:border-box;margin:0;padding:0}
  html,body{width:1200px;height:1200px;overflow:hidden;background:var(--backdrop)}
  body{position:relative;font-family:"Roboto Condensed",sans-serif;color:var(--ink)}
  .card{position:absolute;top:32px;width:500px;height:1126px;background:var(--paper);overflow:hidden;box-shadow:0 4px 14px rgba(0,0,0,.25)}
  .card--front{left:76px}
  .card--back{left:632px}

  /* front */
  .hero-photo{position:absolute;left:0;top:184px;width:500px;height:568px;
    background:linear-gradient(180deg,#ffffff 0%,#f2f1ef 14%,#c9c1b4 30%,#8a8a6c 42%,#9d9384 55%,#8c8378 75%,#7a7068 100%)}
  .title{position:absolute;left:0;top:40px;width:500px;height:180px;font-weight:400}
  .title__line{position:absolute;font-family:"Yellowtail",cursive;line-height:1;white-space:nowrap;font-weight:400}
  .title__line--one{left:38px;top:10px;font-size:58px;color:var(--ink);transform:rotate(-4deg);transform-origin:left center}
  .title__line--two{left:120px;top:78px;font-size:60px;color:var(--green)}
  .title__swoosh{position:absolute;left:220px;top:150px}
  .group-head{position:absolute;left:0;top:228px;width:500px;text-align:center;font-family:"Marcellus",serif;color:var(--ink);white-space:nowrap}
  .group-head__name{font-size:28px;line-height:1.1}
  .group-head__led{font-size:14px;line-height:1.1}
  .group-head__leader{font-size:35px;line-height:1.3;margin-top:2px}

  .facts{position:absolute;left:0;top:752px;width:500px;height:104px;background:var(--green);font-family:"Marcellus",serif;white-space:nowrap}
  .facts__weeks{position:absolute;left:20px;top:14px;width:150px;text-align:center}
  .facts__num{width:54px;height:54px;border-radius:50%;background:#fff;margin:0 auto;font-size:32px;line-height:56px;color:var(--ink)}
  .facts__label{font-size:20px;line-height:24px;margin-top:4px;color:var(--ink);white-space:nowrap}
  .facts__divider{position:absolute;left:191px;top:28px;width:1px;height:60px;background:rgba(255,255,255,.5)}
  .facts__cost{position:absolute;left:220px;top:22px;color:#fff;font-size:33px;line-height:1}
  .facts__size{position:absolute;left:220px;top:62px;font-size:16px;color:var(--ink)}

  .topics__head{position:absolute;left:0;top:866px;width:500px;display:flex;align-items:center;gap:12px}
  .topics__rule{flex:1;height:2px;background:linear-gradient(90deg,transparent,var(--green))}
  .topics__rule--r{background:linear-gradient(90deg,var(--green),transparent)}
  .topics__title{font-weight:700;font-size:26px;color:var(--green);white-space:nowrap}
  .topics__col{position:absolute;top:910px;list-style:none;font-size:17px;line-height:21px;white-space:nowrap}
  .topics__col--left{left:28px}
  .topics__col--right{left:263px;top:912px}
  .topics__col li{position:relative;padding-left:20px}
  .topics__col li::before{content:"";position:absolute;left:0;top:6px;width:11px;height:11px;border-radius:50%;background:var(--green)}

  .contact{position:absolute;left:0;bottom:0;width:500px;height:78px;background:var(--green);text-align:center;font-weight:700;font-size:23px;line-height:28px;padding-top:10px;white-space:nowrap}

  /* back */
  .letter{position:absolute;left:48px;top:80px;width:428px}
  .letter__headline{font-weight:700;font-size:29px;color:var(--green);line-height:1.2;white-space:nowrap}
  .letter__lead{font-weight:700;font-size:15px;line-height:25px;margin-top:4px}
  .letter__body{font-size:15px;line-height:25.5px;margin-top:25px}
  .letter__sign{font-family:"Marcellus",serif;font-size:16px;text-align:right;margin-top:10px}

  .bio{position:absolute;left:0;top:517px;width:500px;height:609px;background:var(--green);color:#fff}
  .bio__band{position:absolute;left:0;bottom:0}
  .bio__portrait{position:absolute;left:24px;top:29px;width:152px;height:152px;border-radius:50%;border:5px solid #fff;
    background:radial-gradient(circle at 50% 40%,#c9b8a4 0%,#8f98a8 60%,#6c7687 100%)}
  .bio__name{position:absolute;left:204px;top:46px;font-weight:700;font-style:italic;font-size:22px;white-space:nowrap}
  .bio__text{position:absolute;left:204px;top:78px;width:282px;font-size:15px;line-height:25.5px}
  .bio__more{position:absolute;left:38px;top:192px;width:440px;font-size:15px;line-height:20px}

  .biz{position:absolute;left:32px;top:275px;width:464px;height:250px;background:#fff;box-shadow:0 10px 16px rgba(0,0,0,.35);color:var(--ink)}
  .biz__brand{position:absolute;left:18px;top:96px;width:164px;display:flex;align-items:center;gap:8px;font-size:17px;line-height:21px;color:var(--green)}
  .biz__dot{flex:0 0 14px;width:14px;height:14px;border-radius:50%;background:var(--green)}
  .biz__line{position:absolute;left:196px;top:40px;width:1px;height:176px;background:var(--teal-line)}
  .biz__info{position:absolute;left:216px;top:48px;width:240px;white-space:nowrap}
  .biz__name{font-family:"Marcellus",serif;font-size:20px}
  .biz__role{font-size:10px;color:var(--green);line-height:15px;padding-left:12px}
  .biz__contact{font-size:12px;line-height:18px;margin-top:30px;padding-left:12px}
</style>
</head>
<body>

<section class="card card--front">
  <div class="hero-photo" role="img" aria-label="Photo of a smiling woman sitting barefoot on a rock on a beach at dusk, dunes and wooden stairs behind"></div>

  <h1 class="title">
    <span class="title__line title__line--one">Mending the</span>
    <span class="title__line title__line--two">Weary Spirit</span>
    <svg class="title__swoosh" width="260" height="30" viewBox="0 0 260 30" aria-hidden="true">
      <path d="M2 28 C80 10 170 4 258 8 L258 12 C170 10 90 16 2 28 Z" fill="var(--green)"/>
    </svg>
  </h1>

  <div class="group-head">
    <p class="group-head__name">Women's Trauma &amp; Loss Group</p>
    <p class="group-head__led">Led by Licensed Professional Counselor,</p>
    <p class="group-head__leader">Jen Dalby Rusk</p>
  </div>

  <div class="facts">
    <div class="facts__weeks">
      <div class="facts__num">10</div>
      <div class="facts__label">Week Group</div>
    </div>
    <div class="facts__divider"></div>
    <p class="facts__cost">Cost - $35 session</p>
    <p class="facts__size">Group size limited to 10 participants</p>
  </div>

  <div class="topics__head">
    <span class="topics__rule"></span>
    <h2 class="topics__title">Topics Include</h2>
    <span class="topics__rule topics__rule--r"></span>
  </div>
  <ul class="topics__col topics__col--left">
    <li>What is Trauma?</li>
    <li>How Trauma Affects Us</li>
    <li>Creating a Feeling of Safety</li>
    <li>Managing Trauma Triggers</li>
    <li>Importance of Self Care</li>
    <li>Healthy vs. Unhealthy Coping</li>
  </ul>
  <ul class="topics__col topics__col--right">
    <li>Guilt, Shame, and Blame</li>
    <li>Victim vs. Victimized</li>
    <li>Grieving through Loss</li>
    <li>Anger and Forgiveness</li>
    <li>Imagining a Better Future</li>
  </ul>

  <footer class="contact">
    <p>Jen Dalby Rusk, LPC, LMFT</p>
    <p>(555) 614-3920 &nbsp;|&nbsp; jen@brightmeadowcare.example</p>
  </footer>
</section>

<section class="card card--back">
  <div class="letter">
    <h2 class="letter__headline">Life hurts and does not seem fair.</h2>
    <p class="letter__lead">So what do you do when you are faced with an event in your life that knocks you off your feet?</p>
    <p class="letter__body">It seems no one understands what you are feeling and no one knows just what to say. It is tempting to pull away and isolate or put up a mask and pretend everything is OK.</p>
    <p class="letter__body">It is my desire you know that you are not alone! There are others who understand the feelings you are going through and offer a safe place for encouraging support. I want to invite you to embark on a courageous journey of healing where you will not only learn how to "survive" after trauma and loss, but instead, learn that you can once again "thrive"!</p>
    <p class="letter__sign">- Jen Dalby Rusk, LPC, LMFT</p>
  </div>

  <div class="bio">
    <svg class="bio__band" width="500" height="609" viewBox="0 0 500 609" aria-hidden="true">
      <polygon points="0,450 500,390 500,609 0,609" fill="var(--lime)"/>
    </svg>
    <div class="bio__portrait" role="img" aria-label="Round portrait photo of the counselor"></div>
    <h3 class="bio__name">Jen Dalby Rusk</h3>
    <p class="bio__text">is a Licensed Professional Counselor and Licensed Marriage and Family Therapist. She is the owner of Quiet Harbor Counseling Services located in Tulsa, OK.</p>
    <p class="bio__more">Jen is a trauma survivor herself and understands firsthand the unique challenges that can arise on the journey to healing.</p>

    <div class="biz">
      <div class="biz__brand"><span class="biz__dot"></span><span>Quiet Harbor Counseling</span></div>
      <div class="biz__line"></div>
      <div class="biz__info">
        <p class="biz__name">Jen Rusk, LPC-S, LMFT</p>
        <p class="biz__role">Licensed Professional Counselor</p>
        <p class="biz__role">Licensed Marriage and Family Therapist</p>
        <p class="biz__contact">555.614.3920<br>jen@brightmeadowcare.example</p>
      </div>
    </div>
  </div>
</section>

</body>
</html>
```